Quarveling stickers design for our main topics (for example: agile and Kanban)

We are looking for sticker design, that will reflect our cooperate identity and can be used for the different topics in our company. We would like to start with our Agile Coaching Offers with a Kanban Sticker saying "stop starting, start finishing", A bad example can be find in the file upload ;)
Check out our homepage to get a feeling for the cooperate identity (www.quarveling.ch)

Target Market(s)

Customers and trainees from our trainings

Industry/Entity Type

Consulting

Colors
0355a3
fbed22

Requirements
Must have
• a cool design thats fits to our customer design
the 2 lines can be changed for future stickers ... like in the example "stop starting, start finishing" and "we show you how"
Nice to have
• -
Should not have
• -

```html
<!DOCTYPE html>
<html lang="en">
<head>
<meta charset="utf-8">
<title>Quarveling Kanban Coaching Sticker</title>
<link rel="stylesheet" href="https://fonts.googleapis.com/css2?family=PT+Sans:wght@400;700&display=swap">
<style>
  :root {
    --page-bg: #f4f4f4;
    --sticker-bg: #d0daee;
    --brand-blue: #3a55a8;
    --brand-yellow: #f9f4a0;
  }
  html, body {
    margin: 0;
    padding: 0;
    overflow: hidden;
  }
  .canvas {
    width: 1200px;
    height: 928px;
    background: var(--page-bg);
    display: flex;
    align-items: center;
    justify-content: center;
    overflow: hidden;
  }
  .sticker {
    width: 640px;
    height: 640px;
    display: block;
  }
  .sticker-face { fill: var(--sticker-bg); }
  .sticker-ring {
    fill: none;
    stroke: var(--brand-yellow);
    stroke-width: 4;
  }
  .target-illustration { fill: var(--brand-yellow); }
  .topic-label {
    font-family: "PT Sans", sans-serif;
    font-size: 36px;
    letter-spacing: 8px;
    fill: var(--brand-blue);
  }
  .slogan-strong {
    font-family: "PT Sans", sans-serif;
    font-weight: 700;
    font-size: 78px;
    fill: var(--brand-blue);
  }
  .slogan-light {
    font-family: "PT Sans", sans-serif;
    font-weight: 400;
    font-size: 58px;
    fill: var(--brand-blue);
  }
  .brand-mark { fill: var(--brand-blue); }
  .brand-name {
    font-family: "PT Sans", sans-serif;
    font-weight: 400;
    font-size: 32px;
    letter-spacing: 2px;
    fill: var(--brand-blue);
  }
</style>
</head>
<body>
<main class="canvas">
  <svg class="sticker" viewBox="0 0 660 660" xmlns="http://www.w3.org/2000/svg">
    <defs>
      <path id="topic-arc" d="M 60 330 A 270 270 0 0 1 600 330"/>
    </defs>

    <circle class="sticker-face" cx="330" cy="330" r="330"/>

    <text class="topic-label">
      <textPath href="#topic-arc" startOffset="50%" text-anchor="middle">KANBAN COACHING</textPath>
    </text>

    <path class="sticker-ring" d="M 99 247 A 245 245 0 0 1 575 330"/>
    <path class="sticker-ring" d="M 557 422 A 245 245 0 0 1 85 340"/>

    <g class="target-illustration" role="img" aria-label="Target with an arrow in the bullseye">
      <circle cx="330" cy="330" r="158"/>
    </g>

    <text class="slogan-strong" x="47" y="322">STOP</text>
    <text class="slogan-light" x="237" y="322">starting</text>
    <text class="slogan-strong" x="170" y="392">START</text>
    <text class="slogan-light" x="392" y="392">finishing</text>

    <rect class="brand-mark" x="310" y="522" width="40" height="40"/>
    <text class="brand-name" x="330" y="606" text-anchor="middle">Quarveling</text>
  </svg>
</main>
</body>
</html>
```